Harlow Stonefield Civil Construction website design

We want a Bold website to promote our Heavy Civil Construction company, We would like an organic / tangible feel to the site. The pictures will be over saturated so they pop. We need to be able to easliy upload new projects and pictures on a regular basis.
Home page will have a full screen width image, "home page image" with silhouette and logo. It will also have about us area and picture
Page 2 will be Project Gallery with pictures in project folders
Page 3 will be an employment application form and submission
Page 4 will be Contact Us
Target Market(s)
Construction indusrty
Industry/Entity Type
Contractor
Coding
Coded - Design and coding required
Number of Pages Required
4 page
Font styles to use
Other font styles liked:
- Hypatia Sans Pro Light
Look and feel

```html
<!DOCTYPE html>
<html lang="en">
<head>
<meta charset="utf-8">
<title>Harlow Stonefield Civil Construction</title>
<link href="https://fonts.googleapis.com/css2?family=Jost:wght@300;400;500;600;700&display=swap" rel="stylesheet">
<style>
:root{
  --blue:#3553a7;
  --blue-dark:#2c468f;
  --ink:#111;
  --text:#333;
  --muted:#555;
  --gray-band:#f4f4f4;
  --footer:#1b1b1b;
  --white:#fff;
}
*{box-sizing:border-box;margin:0;padding:0}
html,body{width:1200px;height:3011px;overflow:hidden;background:var(--white);font-family:"Jost",sans-serif;color:var(--text)}
.page{position:relative;width:1200px;height:3011px}
.abs{position:absolute}

/* header */
.brand{display:flex;align-items:center;gap:12px}
.brand-mark{width:44px;height:44px;border:3px solid var(--blue)}
.brand-name{font-weight:500;color:var(--blue);line-height:1.1;font-size:19px;letter-spacing:.5px}
.brand-name small{display:block;font-size:13px;letter-spacing:4px}
.contact{display:flex;align-items:center;gap:12px;font-size:13px;color:#222;line-height:1.6}
.contact small{font-size:11px;display:block}
.contact-icon{width:36px;height:36px;border-radius:50%;background:var(--blue);display:flex;align-items:center;justify-content:center}
.socials{display:flex;gap:17px}
.social-link{display:block;width:15px;height:15px;border-radius:50%;border:1.5px solid #555}

/* nav */
.nav{top:106px;left:0;width:1200px;height:42px;background:var(--blue)}
.nav a{position:absolute;top:12px;color:var(--white);font-size:14px;font-weight:300;text-decoration:none}

/* hero */
.hero{top:148px;left:0;width:1200px;height:660px;background:linear-gradient(180deg,#5f7896 0%,#8a97a4 32%,#8b7442 58%,#5d4a34 80%,#3c3227 100%)}
.hero-shade{top:148px;left:0;width:1200px;height:660px;background:rgba(20,25,40,.35)}
.hero-title{top:405px;left:0;width:1200px;text-align:center;color:var(--white);font-size:70px;font-weight:600;letter-spacing:1px}
.hero-text{top:490px;left:280px;width:640px;text-align:center;color:var(--white);font-size:14px;font-weight:300;line-height:29px}
.btn{display:flex;align-items:center;justify-content:center;background:var(--blue);color:var(--white);font-weight:300;border-radius:5px;text-decoration:none}
.dot{top:693px;width:16px;height:16px;border-radius:50%;border:1.5px solid var(--white)}

/* about */
.about-photo{top:858px;left:165px;width:367px;height:379px;background:linear-gradient(160deg,#4f7fc8 0%,#8cb1db 35%,#c7a548 60%,#5a4a3a 100%)}
.h2{font-weight:600;color:var(--ink)}
.about-text{top:968px;left:587px;width:470px;font-size:10.6px;line-height:24px;font-weight:300;letter-spacing:-.1px}

/* projects */
.tabs{top:1548px;left:146px;height:41px;display:flex;border:1px solid var(--blue);border-radius:4px;overflow:hidden}
.tabs span{display:flex;align-items:center;justify-content:center;font-size:11.5px;width:69px;border-left:1px solid var(--blue);color:#222;background:var(--white)}
.tabs span.active{background:var(--blue);color:var(--white);width:79px;border-left:none}
.arrow-btn{top:1552px;width:34px;height:32px;background:var(--white);border-radius:4px;display:flex;align-items:center;justify-content:center;box-shadow:0 1px 3px rgba(0,0,0,.08)}
.card{width:211px;height:179px;border-radius:20px;overflow:hidden}
.card-label{font-size:14px;color:#444;font-weight:300}
.overlay{position:absolute;inset:0;background:rgba(30,32,38,.78);padding:40px 20px;color:var(--white);font-size:11px;line-height:21px;font-weight:300}
.overlay .btn{background:var(--white);color:var(--blue);width:78px;height:25px;font-size:9.5px;margin-top:14px;border-radius:3px}

.divider{display:flex;align-items:center;gap:10px}
.divider i{display:block;width:69px;height:1px}
.divider b{display:block;width:34px;height:34px;border:3px solid}

/* footer */
.footer{top:2665px;left:0;width:1200px;height:308px;background:var(--footer)}
.foot-nav a{position:absolute;top:2834px;color:var(--white);font-size:14px;font-weight:300;text-decoration:none}
.foot-social{display:block;top:2888px;width:38px;height:38px;border-radius:50%;border:1.5px solid var(--white);background:var(--blue)}
.bottom-bar{top:2973px;left:0;width:1200px;height:38px;background:var(--blue);color:var(--white);font-size:11px;font-weight:300}
</style>
</head>
<body>
<div class="page">

  <!-- header -->
  <div class="abs brand" style="top:22px;left:182px">
    <div class="brand-mark"></div>
    <div class="brand-name">HARLOW STONEFIELD<small>CIVIL CONSTRUCTION</small></div>
  </div>
  <div class="abs contact" style="top:33px;left:574px">
    <div class="contact-icon"><svg width="14" height="14" viewBox="0 0 24 24"><path fill="#fff" d="M6.6 10.8a15 15 0 0 0 6.6 6.6l2.2-2.2a1 1 0 0 1 1-.25 11.4 11.4 0 0 0 3.6.57 1 1 0 0 1 1 1V20a1 1 0 0 1-1 1A17 17 0 0 1 3 4a1 1 0 0 1 1-1h3.5a1 1 0 0 1 1 1c0 1.25.2 2.45.57 3.57a1 1 0 0 1-.25 1z"/></svg></div>
    <div><small>Call Us!</small>555-014-2290</div>
  </div>
  <div class="abs contact" style="top:33px;left:719px">
    <div class="contact-icon"><svg width="14" height="12" viewBox="0 0 24 18"><path fill="#fff" d="M0 2l12 8 12-8V0H0zm0 3v13h24V5l-12 8z"/></svg></div>
    <div><small>Email Us!</small>info@harlowstonefield.com</div>
  </div>
  <div class="abs socials" style="top:43px;left:927px">
    <a class="social-link" href="#" aria-label="Social profile: news page" title="News page"></a>
    <a class="social-link" href="#" aria-label="Social profile: updates feed" title="Updates feed"></a>
    <a class="social-link" href="#" aria-label="Social profile: community page" title="Community page"></a>
    <a class="social-link" href="#" aria-label="Social profile: photo gallery" title="Photo gallery"></a>
  </div>

  <!-- nav -->
  <nav class="abs nav">
    <a href="#" style="left:168px">Home</a>
    <a href="#" style="left:264px">About Us</a>
    <a href="#" style="left:378px">Gallery</a>
    <a href="#" style="left:479px">Employment</a>
    <a href="#" style="left:609px">Contact Us</a>
    <svg class="abs" style="top:14px;left:1020px" width="14" height="14" viewBox="0 0 24 24"><circle cx="10" cy="10" r="7" fill="none" stroke="#fff" stroke-width="3"/><path d="M15 15l7 7" stroke="#fff" stroke-width="3"/></svg>
  </nav>

  <!-- hero -->
  <div class="abs hero" role="img" aria-label="Yellow excavator digging at a construction site under a cloudy sky"></div>
  <div class="abs hero-shade"></div>
  <h1 class="abs hero-title">HARLOW STONEFIELD</h1>
  <p class="abs hero-text">Lorem Ipsum is simply dummy text of the printing and typesetting industry. Lorem Ipsum has been the industry's standard dummy text ever since the 1500s, when an unknown printer</p>
  <a class="abs btn" href="#" style="top:567px;left:534px;width:133px;height:50px;font-size:14px;border:1px solid #fff">Learn More</a>
  <span class="abs dot" style="left:568px"></span>
  <span class="abs dot" style="left:592px;background:#fff"></span>
  <span class="abs dot" style="left:615px"></span>
  <svg class="abs" style="top:745px;left:0" width="1200" height="66" viewBox="0 0 1200 66">
    <path d="M0 9 L600 60 L1200 9 L1200 66 L0 66Z" fill="#fff"/>
    <path d="M0 9 L600 60 L1200 9" fill="none" stroke="#bbb" stroke-width="3"/>
  </svg>

  <!-- about -->
  <div class="abs about-photo" role="img" aria-label="Excavator at work on a sunny job site"></div>
  <h2 class="abs h2" style="top:878px;left:586px;font-size:42px">About Us</h2>
  <div class="abs" style="top:935px;left:586px;width:110px;height:2px;background:var(--blue)"></div>
  <p class="abs about-text">Lorem Ipsum is simply dummy text of the printing and typesetting industry. Lorem Ipsum has been the industry's standard dummy text ever since the 1500s, when an unknown printer took a galley of type and scrambled it to make a type specimen book. It has survived not only five centuries, but also the leap into electronic typesetting, remaining essentially unchanged. It was popularised in the 1960s with the release of Letraset sheets containing Lorem Ipsum passages, and more recently with desktop publishing software like Aldus PageMaker including versions of Lorem Ipsum.</p>
  <a class="abs btn" href="#" style="top:1141px;left:588px;width:118px;height:40px;font-size:12px">Learn More</a>

  <!-- projects band -->
  <svg class="abs" style="top:1275px;left:0" width="1200" height="960" viewBox="0 0 1200 960">
    <path d="M0 0 L600 63 L1200 0 L1200 880 L600 957 L0 880Z" fill="#f4f4f4"/>
  </svg>
  <h2 class="abs h2" style="top:1393px;left:0;width:1200px;text-align:center;font-size:40px">Our Latest Project</h2>
  <div class="abs divider" style="top:1461px;left:504px;color:var(--blue)">
    <i style="background:var(--blue)"></i><b></b><i style="background:var(--blue)"></i>
  </div>
  <div class="abs tabs">
    <span class="active">All Project</span><span>Lorem</span><span>Lorem</span><span>Lorem</span><span>Lorem</span>
  </div>
  <div class="abs arrow-btn" style="left:938px"><svg width="10" height="12" viewBox="0 0 10 12"><path d="M7 1 2 6l5 5" fill="none" stroke="#3553a7" stroke-width="2"/></svg></div>
  <div class="abs arrow-btn" style="left:987px"><svg width="10" height="12" viewBox="0 0 10 12"><path d="M3 1l5 5-5 5" fill="none" stroke="#3553a7" stroke-width="2"/></svg></div>

  <div class="abs card" style="top:1645px;left:143px;background:linear-gradient(160deg,#6a6b55,#8d8878,#4b4638)" role="img" aria-label="Loader dumping gravel at a utility dig"></div>
  <div class="abs card" style="top:1645px;left:378px;background:linear-gradient(180deg,#6f7a84,#3d3a2e)" role="img" aria-label="Equipment on a cleared lot at dusk">
    <div class="overlay">Lorem Ipsum is simply dummy text of the printing and typesetting industry.<a class="btn" href="#">Learn More</a></div>
  </div>
  <div class="abs card" style="top:1645px;left:612px;background:linear-gradient(160deg,#8f9b88,#6f7c5e,#3e5a3a)" role="img" aria-label="Aerial view of a site development next to a pond"></div>
  <div class="abs card" style="top:1645px;left:847px;background:linear-gradient(160deg,#b7b0a4,#c2a64a,#6c6356)" role="img" aria-label="Bulldozer grading sandy soil"></div>
  <span class="abs card-label" style="top:1838px;left:171px">Project 1</span>
  <span class="abs card-label" style="top:1838px;left:406px">Project 1</span>
  <span class="abs card-label" style="top:1838px;left:640px">Project 1</span>
  <span class="abs card-label" style="top:1838px;left:875px">Project 1</span>

  <div class="abs card" style="top:1885px;left:143px;background:linear-gradient(160deg,#8a7560,#c59a2e,#6f6a5c)" role="img" aria-label="Worker in a trench box laying pipe"></div>
  <div class="abs card" style="top:1885px;left:378px;background:linear-gradient(180deg,#9fb2c6,#6d6a5e,#4f4a3e)" role="img" aria-label="Crew installing a trench shield beside a truck"></div>
  <div class="abs card" style="top:1885px;left:612px;background:linear-gradient(180deg,#4e6b3a,#9a9a90,#2d3a4c)" role="img" aria-label="Completed drainage channel with concrete blocks"></div>
  <div class="abs card" style="top:1885px;left:847px;background:linear-gradient(180deg,#6a95d0,#7c8f5c,#8b8d8e)" role="img" aria-label="Long reach excavator placing stone at a pond"></div>
  <span class="abs card-label" style="top:2078px;left:171px">Project 1</span>
  <span class="abs card-label" style="top:2078px;left:406px">Project 1</span>
  <span class="abs card-label" style="top:2078px;left:640px">Project 1</span>
  <span class="abs card-label" style="top:2078px;left:875px">Project 1</span>

  <!-- employment -->
  <h2 class="abs h2" style="top:2284px;left:0;width:1200px;text-align:center;font-size:40px">Employment</h2>
  <div class="abs divider" style="top:2356px;left:504px">
    <i style="background:#111"></i><b style="border-color:#111"></b><i style="background:#111"></i>
  </div>
  <p class="abs" style="top:2418px;left:222px;width:756px;text-align:center;font-size:11.2px;line-height:29px;font-weight:300;letter-spacing:-.1px">Lorem Ipsum is simply dummy text of the printing and typesetting industry. Lorem Ipsum has been the industry's standard dummy text ever since the 1500s, when an unknown printer took a galley of type and scrambled it to make a type specimen book. It has survived not only five centuries, but also the leap into electronic type-setting, remaining essentially unchanged. It was popularised in the 1960s with the release of Letraset sheets containing Lorem Ipsum passages, and more recently with desktop publishing software like Aldus PageMaker including versions of Lorem Ipsum.</p>
  <a class="abs btn" href="#" style="top:2560px;left:534px;width:133px;height:41px;font-size:12px">Emplyment Form</a>

  <!-- footer -->
  <footer class="abs footer"></footer>
  <div class="abs brand" style="top:2738px;left:458px">
    <div class="brand-mark" style="border-color:#fff;width:50px;height:50px"></div>
    <div class="brand-name" style="color:#fff;font-size:22px">HARLOW STONEFIELD<small style="font-size:14px">CIVIL CONSTRUCTION</small></div>
  </div>
  <div class="foot-nav">
    <a href="#" style="left:361px">Home</a>
    <a href="#" style="left:451px">About Us</a>
    <a href="#" style="left:559px">Gallery</a>
    <a href="#" style="left:653px">Employment</a>
    <a href="#" style="left:777px">Contact Us</a>
  </div>
  <a class="abs foot-social" href="#" style="left:528px" aria-label="Social profile: news page" title="News page"></a>
  <a class="abs foot-social" href="#" style="left:581px" aria-label="Social profile: updates feed" title="Updates feed"></a>
  <a class="abs foot-social" href="#" style="left:633px" aria-label="Social profile: photo gallery" title="Photo gallery"></a>
  <div class="abs bottom-bar">
    <span class="abs" style="top:12px;left:170px">© Copyright 2019 Harlow Stonefield</span>
    <span class="abs" style="top:12px;left:897px">Privacy Policy &nbsp;|&nbsp; Site map</span>
  </div>
</div>
</body>
</html>
```